Minimalistic and chic product labels required for tea packaging

We need a Label Sticker Design for our tea company that is minimalistic, simple and chic.

We have 2 categories of tea: artisan tea (single flavoured tea e.g. green and black) and herbal teas (e.g. mixuture of herbs and flowers). We would like to have the designs to tell the difference of artisan tea and herbal tea, this can be done by having different colours to tell the difference or if there are other design features used.

We would also like to have colourful colours on our herbal tea range, preferably either a light and chic pastel colour palette or bright and chic colour palette.

The labels will be stuck onto a white pouch. The final design should also include the variety of colour palettes that can be used in AI format with the label. Preferred label measurements in 9cm width, and 11cm height. Our logo is attached.

Beauty and wellness

Health And Wellness

Requirements
Must have
• 2 x labels (front and back)
Front label must include logo, text to include tea type and weight
Back label must include text space to write description
Nice to have
• Simple and chic label design to stick onto a white pouch
Should not have
• Must not have too much graphic and pictures

```html
<!DOCTYPE html>
<html lang="en">
<head>
<meta charset="utf-8">
<title>Fernleaf Tea Labels</title>
<link href="https://fonts.googleapis.com/css2?family=Allura&family=Nunito+Sans:wght@300;400&display=swap" rel="stylesheet">
<style>
  :root {
    --paper: #ffffff;
    --ink: #4f4f4f;
    --mint: #d9ebe8;
    --mint-accent: #7fa89b;
    --blush: #f8e2da;
    --blush-accent: #e6b4a9;
    --text-font: "Nunito Sans", Arial, sans-serif;
    --script-font: "Allura", cursive;
  }
  html, body {
    margin: 0;
    padding: 0;
    width: 996px;
    height: 1200px;
    overflow: hidden;
    background: var(--paper);
  }
  .artboard {
    position: relative;
    width: 1196px;
    height: 1440px;
    transform: scale(0.8328);
    transform-origin: 0 0;
  }
  .label {
    position: absolute;
    width: 532px;
    height: 650px;
    overflow: hidden;
  }
  .label--artisan { background: var(--mint); --accent: var(--mint-accent); }
  .label--herbal { background: var(--blush); --accent: var(--blush-accent); }
  .label--left { left: 40px; }
  .label--right { left: 623px; }
  .label--front { top: 33px; }
  .label--back { top: 744px; }

  .hexagon {
    position: absolute;
    inset: 0;
    width: 532px;
    height: 650px;
  }
  .hexagon polygon { fill: var(--paper); }

  .brand {
    position: absolute;
    left: 0;
    width: 100%;
    text-align: center;
    font-family: var(--text-font);
    font-weight: 300;
    color: var(--ink);
    letter-spacing: 0.12em;
  }
  .label--front .brand { top: 196px; font-size: 34px; }
  .label--back .brand { top: 508px; font-size: 28px; }
  .brand-mark {
    position: absolute;
    left: 50%;
    width: 14px;
    height: 14px;
    margin-left: -7px;
    border-radius: 50%;
    background: var(--accent);
  }
  .label--front .brand-mark { top: 170px; }
  .label--back .brand-mark { top: 484px; }

  .tea-range {
    position: absolute;
    top: 388px;
    left: 0;
    width: 100%;
    text-align: center;
    font-family: var(--script-font);
    font-size: 84px;
    line-height: 1;
    color: var(--ink);
  }
  .tea-flavour {
    position: absolute;
    top: 474px;
    left: 0;
    width: 100%;
    text-align: center;
    font-family: var(--text-font);
    font-weight: 300;
    font-size: 20px;
    letter-spacing: 0.42em;
    text-indent: 0.42em;
    color: var(--ink);
  }
  .divider {
    position: absolute;
    top: 540px;
    left: 246px;
    width: 40px;
    height: 2px;
    background: var(--accent);
  }
  .weight {
    position: absolute;
    top: 556px;
    left: 0;
    width: 100%;
    text-align: center;
    font-family: var(--text-font);
    font-size: 18px;
    color: var(--ink);
  }
  .description {
    position: absolute;
    top: 164px;
    left: 66px;
    width: 400px;
    margin: 0;
    text-align: center;
    font-family: var(--text-font);
    font-weight: 300;
    font-size: 16.5px;
    line-height: 25px;
    color: #222;
  }
  .social {
    position: absolute;
    top: 566px;
    left: 0;
    width: 100%;
    text-align: center;
    font-family: var(--text-font);
    font-size: 14px;
    color: var(--accent);
    letter-spacing: 0.05em;
  }
</style>
</head>
<body>
<main class="artboard">

  <section class="label label--artisan label--left label--front" role="img" aria-label="Mint label ground with faint script pattern">
    <svg class="hexagon" viewBox="0 0 532 650" aria-hidden="true"><polygon points="266,27 510,113 510,535 266,623 22,535 22,113"/></svg>
    <span class="brand-mark"></span>
    <div class="brand">FERNLEAF</div>
    <h1 class="tea-range" style="margin:0;font-weight:400">Artisan Tea</h1>
    <div class="tea-flavour">GREEN TEA</div>
    <span class="divider"></span>
    <div class="weight">50g</div>
  </section>

  <section class="label label--herbal label--right label--front" role="img" aria-label="Blush label ground with faint script pattern">
    <svg class="hexagon" viewBox="0 0 532 650" aria-hidden="true"><polygon points="266,27 510,113 510,535 266,623 22,535 22,113"/></svg>
    <span class="brand-mark"></span>
    <div class="brand">FERNLEAF</div>
    <h1 class="tea-range" style="margin:0;font-weight:400">Herbal Teas</h1>
    <div class="tea-flavour">CINNAMON</div>
    <span class="divider"></span>
    <div class="weight">50g</div>
  </section>

  <section class="label label--artisan label--left label--back" role="img" aria-label="Mint label ground with faint script pattern">
    <svg class="hexagon" viewBox="0 0 532 650" aria-hidden="true"><polygon points="266,27 510,113 510,535 266,623 22,535 22,113"/></svg>
    <p class="description">Lorem ipsum dolor sit amet, consectetuer adipiscing elit, sed diam nonummy nibh euismod tincidunt laoreet dolore magna aliquam erat volutpat. Ut wisi enim ad minim veniam, quis nostrud exerci tation ullamcorper suscipit lobortis nisl ut aliquip ex ea commodo consequat. Duis autem vel eum iriure dolor in hendrerit in vulputate velit esse molestie consequat ut</p>
    <span class="brand-mark"></span>
    <div class="brand">FERNLEAF</div>
    <div class="social">@fernleaftea</div>
  </section>

  <section class="label label--herbal label--right label--back" role="img" aria-label="Blush label ground with faint script pattern">
    <svg class="hexagon" viewBox="0 0 532 650" aria-hidden="true"><polygon points="266,27 510,113 510,535 266,623 22,535 22,113"/></svg>
    <p class="description">Lorem ipsum dolor sit amet, consectetuer adipiscing elit, sed diam nonummy nibh euismod tincidunt laoreet dolore magna aliquam erat volutpat. Ut wisi enim ad minim veniam, quis nostrud exerci tation ullamcorper suscipit lobortis nisl ut aliquip ex ea commodo consequat. Duis autem vel eum iriure dolor in hendrerit in vulputate velit esse molestie consequat ut</p>
    <span class="brand-mark"></span>
    <div class="brand">FERNLEAF</div>
    <div class="social">@fernleaftea</div>
  </section>

</main>
</body>
</html>
```